Store Fixture business needs a buisness card design

We are looking for a business card design for a store fixture company. "KL Shelf Outfitters" we help small businesses with their start up by providing fixtures required to display their products.
It should have a simple yet innovative design in the front, and a refined look to our company.
We would like our logo, to have one of our products "display cases, clothing rack, mannequins" integrated in the design. And the rest of it just a clean look, which gives our address, store hours, and contact number, etc.
The color scheme as seen in the samples can be changed as long as the goal is achieved.
Industry/Entity Type
Business
Contact Information for Business Card
KL Shelf Outfitters
4362 Marlow Ave.
San Antonio,TX 78299
www.klshelfoutfitters.example
klpo@klshelfoutfitter.example
(210) 555-0188
M-F: 9-6pm
Sat: 10-3pm

```html
<!DOCTYPE html>
<html lang="en">
<head>
<meta charset="utf-8">
<title>KL Shelf Outfitters – Business Card</title>
<link rel="stylesheet" href="https://fonts.googleapis.com/css2?family=Roboto+Condensed:wght@700&family=Abel&display=swap">
<style>
  :root {
    --navy: #26468e;
    --cream: #fdfdf1;
    --yellow: #f6e81c;
    --green: #1f9a45;
    --white: #ffffff;
    --page: #ece8e1;
  }
  html, body {
    margin: 0;
    padding: 0;
    width: 1016px;
    height: 1200px;
    overflow: hidden;
    background: var(--page);
  }
  .canvas {
    position: relative;
    width: 1016px;
    height: 1200px;
  }
  .card {
    position: absolute;
    left: 123px;
    width: 770px;
    height: 456px;
    background: var(--cream);
    overflow: hidden;
  }
  .card--front { top: 111px; }
  .card--back { top: 636px; }
  .card__band {
    position: absolute;
    inset: 0;
    width: 100%;
    height: 100%;
  }
  .brand {
    position: absolute;
    display: flex;
    align-items: center;
    gap: 14px;
    font-family: "Roboto Condensed", sans-serif;
    font-weight: 700;
    color: var(--navy);
    white-space: nowrap;
  }
  .brand__mark {
    background: var(--green);
    flex: none;
  }
  .card--front .brand {
    left: 0;
    right: 0;
    top: 110px;
    justify-content: center;
    font-size: 66px;
  }
  .card--front .brand__mark { width: 48px; height: 48px; }
  .services {
    position: absolute;
    left: 0;
    right: 0;
    top: 350px;
    display: flex;
    justify-content: center;
    align-items: center;
    gap: 10px;
    font-family: "Roboto Condensed", sans-serif;
    font-weight: 700;
    font-size: 22px;
    color: var(--white);
  }
  .services__dot {
    width: 9px;
    height: 9px;
    background: var(--yellow);
  }
  .card--back .brand {
    left: 70px;
    top: 58px;
    font-size: 34px;
    gap: 10px;
  }
  .card--back .brand__mark { width: 26px; height: 26px; }
  .hours {
    position: absolute;
    right: 68px;
    top: 44px;
    color: var(--navy);
    text-align: right;
  }
  .hours__title {
    font-family: "Abel", sans-serif;
    font-size: 24px;
    margin-bottom: 10px;
  }
  .hours__row {
    display: flex;
    justify-content: space-between;
    gap: 40px;
    font-family: "Roboto Condensed", sans-serif;
    font-weight: 700;
    font-size: 21px;
    line-height: 27px;
    text-align: left;
  }
  .hours__row span:first-child { width: 150px; }
  .contact {
    position: absolute;
    left: 413px;
    top: 190px;
    color: var(--white);
  }
  .contact__name {
    font-family: "Roboto Condensed", sans-serif;
    font-weight: 700;
    font-size: 25px;
    margin: 0 0 14px;
  }
  .contact__list {
    list-style: none;
    margin: 0;
    padding: 0;
    font-family: "Abel", sans-serif;
    font-size: 22px;
  }
  .contact__item {
    display: flex;
    align-items: flex-start;
    gap: 16px;
    line-height: 31px;
    margin-bottom: 10px;
  }
  .contact__icon {
    width: 22px;
    height: 22px;
    margin-top: 5px;
    flex: none;
  }
</style>
</head>
<body>
<div class="canvas">

  <section class="card card--front" aria-label="Business card front">
    <svg class="card__band" viewBox="0 0 770 456" aria-hidden="true">
      <polygon points="0,298 248,298 285,274 322,298 770,298 770,456 0,456" fill="var(--navy)"/>
      <polyline points="0,293 248,293 285,269 322,293 770,293" fill="none" stroke="var(--yellow)" stroke-width="5"/>
    </svg>
    <div class="brand">
      <span class="brand__mark"></span>
      <span class="brand__name">KL Shelf Outfitters</span>
    </div>
    <div class="services">
      <span>Store Fixtures</span><span class="services__dot"></span>
      <span>Display Fixtures</span><span class="services__dot"></span>
      <span>Display Cases</span><span class="services__dot"></span>
      <span>Gondola Shelving</span>
    </div>
  </section>

  <section class="card card--back" aria-label="Business card back">
    <svg class="card__band" viewBox="0 0 770 456" aria-hidden="true">
      <polygon points="0,166 115,166 152,143 189,166 770,166 770,456 0,456" fill="var(--navy)"/>
      <polyline points="0,161 115,161 152,138 189,161 770,161" fill="none" stroke="var(--yellow)" stroke-width="5"/>
    </svg>
    <div class="brand">
      <span class="brand__mark"></span>
      <span class="brand__name">KL Shelf Outfitters</span>
    </div>
    <div class="hours">
      <div class="hours__title">Working hours:</div>
      <div class="hours__row"><span>Monday - Friday:</span><span>9am - 6pm</span></div>
      <div class="hours__row"><span>Saturday:</span><span>10am - 3pm</span></div>
    </div>
    <div class="contact">
      <h2 class="contact__name">KL Shelf Outfitters</h2>
      <ul class="contact__list">
        <li class="contact__item">
          <svg class="contact__icon" viewBox="0 0 24 24" aria-hidden="true"><path d="M6 2l4 4-2 3c1 3 4 6 7 7l3-2 4 4-3 4C10 22 2 14 2 5z" fill="var(--yellow)"/></svg>
          <span>(210) 555-0188</span>
        </li>
        <li class="contact__item">
          <svg class="contact__icon" viewBox="0 0 24 24" aria-hidden="true"><rect x="2" y="5" width="20" height="14" fill="none" stroke="var(--yellow)" stroke-width="2"/><polyline points="2,5 12,13 22,5" fill="none" stroke="var(--yellow)" stroke-width="2"/></svg>
          <span>klpo@klshelfoutfitter.example</span>
        </li>
        <li class="contact__item">
          <svg class="contact__icon" viewBox="0 0 24 24" aria-hidden="true"><circle cx="12" cy="12" r="10" fill="none" stroke="var(--yellow)" stroke-width="2"/><ellipse cx="12" cy="12" rx="4" ry="10" fill="none" stroke="var(--yellow)" stroke-width="1.5"/><line x1="2" y1="12" x2="22" y2="12" stroke="var(--yellow)" stroke-width="1.5"/></svg>
          <span>www.klshelfoutfitters.example</span>
        </li>
        <li class="contact__item">
          <svg class="contact__icon" viewBox="0 0 24 24" aria-hidden="true"><polygon points="12,3 2,10 22,10" fill="var(--yellow)"/><rect x="4" y="11" width="16" height="10" fill="var(--yellow)"/><rect x="10" y="14" width="4" height="7" fill="var(--navy)"/></svg>
          <span>4362 Marlow Ave.<br>San Antonio,TX 78299</span>
        </li>
      </ul>
    </div>
  </section>

</div>
</body>
</html>
```